Web design for software company

I'm a software developer that designs high end specialist web applications, mobile apps and user friendly applications for medium to large customers. I integrate different systems together within a company and provide web based applications or mobile apps to view and edit information in that web of linked systems.

I currently work alone, basically selling my time on specialist projects, but also build my own software solutions which I eventually want to put into the market.

My company name is Quarrymind (lowercase 'L' for logic) and I work from the Netherlands. I've attached my current logo which is basically just text in VOXbox font. Current colours are mustard yellow and grey, but i'm open to other options to better fit the web design.

I've got a sort of slogan: "Specialized software development" - better ideas are welcome. The slogan in the logo attachment is older.

I'm looking for a site design that reflects my work as being on the cutting edge of technology, but being clear and simple. My thinking with the name Quarrymind is that it refers to the underlying mechanism and logic of software.

The site will not be text heavy, so some kind of large graphic to do with software design is welcome. I expect about 4 or 5 main pages or sections of the site in which i'll eventually add things like a blog or contact info etc.

Industry/Entity Type

It Company

Number of Pages Required

1 page

Font styles to use
Sans Serif

Requirements
Nice to have
• A large graphic or photo relevant to my focus as a software developer. Something that shows connecting of software systems with perhaps a variety of devices/browsers that would display data from that cloud of systems.
• Something like these (allthough these are ugly - but the idea is what i mean):
• http://st4.pixelvaultimg.example/2000817/22458/i/450/pixelvaultimg_224581193-Cloud-computing-user-interface.jpg
• http://business.tallwick.example/images/modules/mobile-device-policy-design-banner.png
• https://www.pagecrafta.example/images/responsive-web-design.jpg
• http://www.brevanto.example/images/web_apps.png
• https://www.keymurra.example/assets/img/product/web-app@2x.png?v2
Should not have
• Photographs of smiling happy people looking at a screen that make it look like it's a huge business with many offices. I'm a one-man company which could perhaps grow a little bit, but i want to focus on my expertise instead of size.

```html
<!DOCTYPE html>
<html lang="en">
<head>
<meta charset="utf-8">
<title>Quarrymind — Specialized Software Development</title>
<link href="https://fonts.googleapis.com/css2?family=Open+Sans:wght@300;400;600;700&family=Lato:wght@300;400;700&display=swap" rel="stylesheet">
<style>
:root{
  --blue:#1a87c9;
  --yellow:#f5b400;
  --orange:#e67e22;
  --navy:#2f3e50;
  --navy-deep:#26323f;
  --card:#2c3440;
  --card-deep:#1f2630;
  --footer:#232a36;
  --footer-bar:#1a1f29;
  --ink:#222;
  --text:#555;
  --muted:#999;
  --pale:#f3f3f4;
  --line:#e5e5e5;
}
*{margin:0;padding:0;box-sizing:border-box}
html,body{width:1200px;height:4412px;overflow:hidden}
body{font-family:"Open Sans",Arial,sans-serif;color:var(--text);background:#fff;position:relative}
section,header,footer,nav{position:absolute;left:0;width:1200px}
.abs{position:absolute}
.center{left:0;width:1200px;text-align:center}
.wordmark{font-family:"Lato",Arial,sans-serif;font-weight:300;letter-spacing:3px}
.ph{position:absolute}

/* hero */
.hero{top:0;height:603px;background:var(--pale);overflow:hidden}
.hero-kicker{top:28px;font-size:22px;font-weight:300;color:#444;letter-spacing:1px}
.hero-title{top:118px;font-size:38px;font-weight:700;color:var(--ink);letter-spacing:.5px}
.btn{display:inline-block;background:var(--yellow);color:#222;font-size:11px;font-weight:700;text-transform:uppercase;text-align:center}
.hero-btn{top:200px;left:538px;width:124px;height:38px;line-height:38px}
.hero-desk{left:0;top:280px;width:360px;height:323px;background:linear-gradient(160deg,#f3f3f4,#e6e7e9)}
.hero-tablet{left:382px;top:330px;width:471px;height:262px;border-radius:14px;background:linear-gradient(180deg,#1d2430,#2d4f78)}
.hero-phone{left:945px;top:362px;width:135px;height:241px;border-radius:18px 18px 0 0;background:linear-gradient(180deg,#f9fafb,#dfe6ee)}

/* nav */
.site-nav{top:603px;height:67px;background:#fff;border-bottom:1px solid var(--line)}
.nav-logo{left:235px;top:18px;font-size:24px;color:var(--blue)}
.nav-menu{right:235px;top:25px;display:flex;gap:26px;align-items:center;font-size:11px;color:#333}

/* welcome */
.welcome{top:670px;height:491px;background:#fff}
.welcome-title{top:50px;font-family:"Lato",Arial,sans-serif;font-size:34px;font-weight:700;color:var(--ink)}
.welcome-logo{top:92px;font-size:44px;color:var(--blue);letter-spacing:6px}
.welcome-text{top:172px;left:300px;width:600px;font-size:10px;line-height:16px;color:#777;text-align:center}
.service{top:253px;width:230px;text-align:center}
.service-icon{width:94px;height:94px;border-radius:50%;background:var(--blue);margin:0 auto;display:flex;align-items:center;justify-content:center}
.service h3{margin-top:24px;font-size:12px;font-weight:600;color:#333}
.service p{margin-top:8px;font-size:9.5px;line-height:15px;color:var(--muted)}

/* portfolio */
.portfolio{top:1161px;height:933px;background:var(--navy)}
.portfolio-title{top:50px;font-size:20px;font-weight:300;color:#fff}
.portfolio-title b{font-weight:700}
.portfolio-logo{top:84px;font-size:26px;color:#fff}
.portfolio-text{top:126px;left:360px;width:480px;font-size:9.5px;line-height:15px;color:#c0c8d2;text-align:center}
.filters{top:184px;left:458px;display:flex;gap:26px;font-size:9px;font-weight:600;color:#fff;align-items:center}
.filters .active{background:var(--yellow);color:#222;padding:5px 10px}
.gallery{top:236px;height:564px;left:0;width:1200px}
.tile{position:absolute}
.slider-arrow{position:absolute;width:13px;height:16px;background:#fff;top:211px}
.load-btn{left:558px;top:836px;width:84px;height:28px;line-height:28px;font-size:9px}

/* blog */
.blog{top:2094px;height:441px;background:#eef0f2;overflow:hidden}
.blog-bg{left:0;top:0;width:1200px;height:441px;background:linear-gradient(180deg,#f3f4f6,#e4e7eb)}
.blog-title{left:235px;top:110px;font-size:26px;font-weight:300;color:#333}
.blog-intro{left:235px;top:152px;width:160px;font-size:9px;line-height:14px;color:var(--muted)}
.round-arrow{width:32px;height:32px;border-radius:50%;display:flex;align-items:center;justify-content:center;top:244px}
.post{top:117px;width:161px;height:274px;background:var(--card)}
.post-img{height:127px}
.post h4{margin:20px 14px 0;font-size:10.5px;font-weight:700;color:#fff}
.post p{margin:8px 14px 0;font-size:8px;line-height:12px;color:#a7afbb}
.post-more{position:absolute;left:0;bottom:0;width:161px;height:38px;display:flex;background:var(--card-deep)}
.post-more span{flex:1;line-height:38px;padding-left:14px;font-size:9px;font-weight:700;color:#fff}
.post-more i{width:38px;display:flex;align-items:center;justify-content:center;background:var(--blue)}
.post.accent .post-more{background:var(--yellow)}
.post.accent .post-more i{background:var(--orange)}

/* featured */
.featured{top:2535px;height:508px;background:linear-gradient(180deg,#3b4b60,#2e3b4c);overflow:hidden}
.featured-title{top:36px;font-size:24px;font-weight:300;color:#fff}
.featured-logo{top:70px;font-size:30px;color:#fff}
.featured-text{top:118px;left:390px;width:420px;font-size:9.5px;line-height:15px;color:#c8d0da;text-align:center}
.featured-phone{left:440px;top:165px;width:280px;height:343px;background:linear-gradient(160deg,#f1f1f1,#c7cfd8)}
.feature{width:190px}
.feature h4{font-size:10.5px;font-weight:600;color:#fff}
.feature p{margin-top:6px;font-size:8.5px;line-height:13px;color:#c0c8d2}
.feature.left{text-align:right;left:192px}
.feature.right{left:820px}
.feature-dot{width:28px;height:28px;border-radius:50%;background:var(--yellow);display:flex;align-items:center;justify-content:center}

/* contact */
.contact{top:3043px;height:558px;background:#fff}
.contact-title{top:62px;font-size:17px;font-weight:700;color:#333}
.contact-title span{font-weight:300}
.contact-sub{top:94px;left:420px;width:360px;font-size:9px;line-height:14px;color:#888;text-align:center}
.studio{left:250px;top:200px;width:320px}
.studio h4{font-size:11px;font-weight:700;color:#333;letter-spacing:.5px}
.studio p{margin-top:10px;font-size:9px;line-height:14px;color:#888}
.studio ul{list-style:none;margin-top:14px}
.studio li{display:flex;align-items:center;gap:10px;font-size:9px;color:#666;height:17px}
.socials{display:flex;gap:7px;margin-top:14px}
.socials i{width:11px;height:11px;border-radius:50%;background:#555}
.field{left:626px;width:321px;background:#e1e5ea;font-size:9px;color:#9aa3ad;padding:9px 12px}
.submit{left:626px;top:456px;width:72px;height:23px;line-height:23px;background:var(--blue);color:#fff;font-size:8.5px;font-weight:700;text-align:center}

/* map */
.map{top:3601px;height:315px;background:linear-gradient(135deg,#cfd6dd,#b9c3cd)}

/* footer */
.site-footer{top:3916px;height:444px;background:var(--footer)}
.fcol{top:34px}
.fcol h5{font-size:13px;font-weight:400;color:#fff;margin-bottom:20px}
.f-logo{font-size:22px;color:#fff;margin-bottom:18px}
.fcol p{font-size:8.5px;line-height:13px;color:#8a93a0}
.f-link{color:var(--blue);font-size:8.5px;margin-top:10px;display:block}
.follow{display:grid;grid-template-columns:1fr 1fr;gap:14px 10px;margin-top:44px;width:170px}
.follow div{display:flex;gap:7px;align-items:center;font-size:8px;line-height:11px;color:#c5ccd6}
.follow i{width:24px;height:24px;flex:none}
.post-mini{display:flex;gap:10px;margin-bottom:22px;width:170px}
.post-mini i{width:34px;height:34px;flex:none;background:#4a5566}
.post-mini b{display:block;font-size:8.5px;color:#fff;margin-bottom:3px}
.post-mini small{display:block;font-size:7.5px;line-height:11px;color:#8a93a0}
.tags{display:flex;flex-wrap:wrap;gap:6px;width:170px}
.tags span{border:1px solid #4a5566;color:#b3bcc8;font-size:8px;padding:4px 7px}
.tags .on{background:var(--blue);border-color:var(--blue);color:#fff}
.links{list-style:none}
.links li{font-size:8.5px;color:#b3bcc8;height:19px;display:flex;align-items:center;gap:8px}
.links li::before{content:"";width:4px;height:4px;background:var(--yellow)}
.photos{display:grid;grid-template-columns:repeat(3,36px);gap:6px}
.photos i{height:36px;background:#5a6578}
.news{display:flex;margin-top:12px}
.news span{width:130px;height:22px;background:#3a4454;font-size:8px;color:#8a93a0;padding:6px 8px}
.news i{width:22px;height:22px;background:var(--blue)}
.footer-bar{top:4360px;height:52px;background:var(--footer-bar)}
.copy{left:235px;top:20px;font-size:8.5px;color:#8a93a0}
.bar-menu{right:235px;top:20px;display:flex;gap:16px;font-size:8.5px;color:#b3bcc8}
.bar-menu .current{color:var(--yellow)}
</style>
</head>
<body>

<header class="hero">
  <div class="abs center hero-kicker">WE SPECIALIST IN</div>
  <h1 class="abs center hero-title">SPECIALIZED SOFTWARE DEVELOPMENT</h1>
  <a class="abs btn hero-btn">Get Started Now</a>
  <div class="ph hero-desk" role="img" aria-label="Desk scene with earphones and a pen on a white surface"></div>
  <div class="ph hero-tablet" role="img" aria-label="Tablet showing a software development website"></div>
  <div class="ph hero-phone" role="img" aria-label="Smartphone showing a mobile app screen"></div>
</header>

<nav class="site-nav">
  <div class="abs wordmark nav-logo">Quarrymind</div>
  <div class="abs nav-menu">
    <span>Home</span><span>About</span><span>Portfolio</span><span>Blog</span><span>Features</span><span>Contact</span>
    <svg width="12" height="12" viewBox="0 0 12 12"><circle cx="5" cy="5" r="3.8" fill="none" stroke="#555" stroke-width="1.3"/><path d="M8 8l3 3" stroke="#555" stroke-width="1.3"/></svg>
  </div>
</nav>

<section class="welcome">
  <h2 class="abs center welcome-title">WELCOME TO</h2>
  <div class="abs center wordmark welcome-logo">Quarrymind</div>
  <p class="abs welcome-text">We build clear and dependable software for growing companies. Every project starts with careful listening, a sharp plan and honest advice, so the finished system fits the way your people already work. We connect existing tools, clean up the data between them and deliver web and mobile views that simply make sense.</p>

  <div class="abs service" style="left:229px">
    <div class="service-icon"><svg width="30" height="26" viewBox="0 0 30 26"><rect x="2" y="2" width="26" height="17" rx="2" fill="none" stroke="#fff" stroke-width="2"/><path d="M10 24h10M15 19v5" stroke="#fff" stroke-width="2"/></svg></div>
    <h3>Web App Development</h3>
    <p>Fast, secure browser tools that bring data from many linked systems into one clear place.</p>
  </div>
  <div class="abs service" style="left:485px">
    <div class="service-icon"><svg width="20" height="32" viewBox="0 0 20 32"><rect x="2" y="2" width="16" height="28" rx="3" fill="none" stroke="#fff" stroke-width="2"/><circle cx="10" cy="25" r="1.5" fill="#fff"/></svg></div>
    <h3>Mobile App Development</h3>
    <p>Native feeling apps that let your team view and edit key information wherever they are.</p>
  </div>
  <div class="abs service" style="left:735px">
    <div class="service-icon"><svg width="30" height="28" viewBox="0 0 30 28"><path d="M4 14a11 11 0 0 1 22 0z" fill="#fff"/><rect x="3" y="16" width="24" height="4" fill="#fff"/><rect x="9" y="22" width="12" height="3" fill="#fff"/></svg></div>
    <h3>Other Custom Development</h3>
    <p>Integration work, custom logic and tailored solutions for specialist business needs.</p>
  </div>
</section>

<section class="portfolio">
  <h2 class="abs center portfolio-title">Special <b>Portfolio</b> Developement</h2>
  <div class="abs center wordmark portfolio-logo">Quarrymind</div>
  <p class="abs portfolio-text">A short look at recent work for clients in logistics, finance and care. Each case shows how linked systems became simple tools for daily use.</p>
  <div class="abs filters"><span class="active">ALL</span><span>WEB APP</span><span>MOBILE APP</span><span>OTHERS</span></div>

  <div class="abs gallery">
    <div class="tile" style="left:0;top:0;width:300px;height:191px;background:linear-gradient(135deg,#e9eaec,#c9cbcf)" role="img" aria-label="Business cards on a grey desk"></div>
    <div class="tile" style="left:300px;top:0;width:303px;height:191px;background:linear-gradient(135deg,#8e9298,#3c4046)" role="img" aria-label="Stationery mockup on a dark surface"></div>
    <div class="tile" style="left:603px;top:0;width:297px;height:191px;background:linear-gradient(135deg,#f7f7f7,#d6d8db)" role="img" aria-label="Website layout printed on paper"></div>
    <div class="tile" style="left:900px;top:0;width:300px;height:191px;background:linear-gradient(135deg,#cfd3d8,#6b717a)" role="img" aria-label="Open magazine spread"></div>
    <div class="tile" style="left:0;top:191px;width:300px;height:185px;background:linear-gradient(135deg,#fafafa,#e2e4e6)" role="img" aria-label="Keyboard and notebook on a white desk"></div>
    <div class="tile" style="left:300px;top:191px;width:303px;height:185px;background:linear-gradient(135deg,#f2f3f4,#c6cbd1)" role="img" aria-label="Smartphones showing an app"></div>
    <div class="tile" style="left:603px;top:191px;width:597px;height:373px;background:linear-gradient(135deg,#f3c623,#e8dcc4 55%,#f4f2ee)" role="img" aria-label="Branded coffee cup and food packaging"></div>
    <div class="tile" style="left:0;top:376px;width:300px;height:188px;background:linear-gradient(135deg,#b9bcc0,#6c7075)" role="img" aria-label="Keyboard and pencil close up"></div>
    <div class="tile" style="left:300px;top:376px;width:303px;height:188px;background:linear-gradient(135deg,#f4f4f4,#cfd1d4)" role="img" aria-label="Wall clock and notebook"></div>
    <div class="slider-arrow" style="left:1166px"></div>
    <div class="slider-arrow" style="left:1182px"></div>
  </div>

  <a class="abs btn load-btn">Load More</a>
</section>

<section class="blog">
  <div class="ph blog-bg" role="img" aria-label="Faded desk with keyboard in the background"></div>
  <h2 class="abs blog-title">Recent Blog</h2>
  <p class="abs blog-intro">Notes on system design, integration and the small choices that keep software easy to use and easy to maintain over many years.</p>
  <div class="abs round-arrow" style="left:235px;background:var(--blue)"><svg width="10" height="10" viewBox="0 0 10 10"><path d="M7 1L3 5l4 4" fill="none" stroke="#fff" stroke-width="1.6"/></svg></div>
  <div class="abs round-arrow" style="left:278px;background:var(--yellow)"><svg width="10" height="10" viewBox="0 0 10 10"><path d="M3 1l4 4-4 4" fill="none" stroke="#fff" stroke-width="1.6"/></svg></div>

  <article class="abs post" style="left:420px">
    <div class="post-img" role="img" aria-label="App screens on a table" style="background:linear-gradient(135deg,#9aa3ad,#4a5260)"></div>
    <h4>Your Blog Title Here</h4>
    <p>A quick read on planning data flows before writing a single line of code for clients.</p>
    <div class="post-more"><span>READ MORE</span><i><svg width="8" height="8" viewBox="0 0 8 8"><path d="M2 1l3 3-3 3" fill="none" stroke="#fff" stroke-width="1.4"/></svg></i></div>
  </article>
  <article class="abs post accent" style="left:609px">
    <div class="post-img" role="img" aria-label="Hooded figure in a dim room" style="background:linear-gradient(135deg,#6f8aa3,#253140)"></div>
    <h4>Your Blog Title Here</h4>
    <p>Why small, focused teams ship better tools and how to keep projects lean and calm.</p>
    <div class="post-more"><span>READ MORE</span><i><svg width="8" height="8" viewBox="0 0 8 8"><path d="M2 1l3 3-3 3" fill="none" stroke="#fff" stroke-width="1.4"/></svg></i></div>
  </article>
  <article class="abs post" style="left:797px">
    <div class="post-img" role="img" aria-label="Coffee cup beside a laptop" style="background:linear-gradient(135deg,#a9c6dc,#3f6a8c)"></div>
    <h4>Your Blog Title Here</h4>
    <p>Linking older systems with new mobile apps without breaking what already works well.</p>
    <div class="post-more"><span>READ MORE</span><i><svg width="8" height="8" viewBox="0 0 8 8"><path d="M2 1l3 3-3 3" fill="none" stroke="#fff" stroke-width="1.4"/></svg></i></div>
  </article>
</section>

<section class="featured" role="img" aria-label="Busy office corridor in dark blue tones">
  <h2 class="abs center featured-title">Featured</h2>
  <div class="abs center wordmark featured-logo">Quarrymind</div>
  <p class="abs featured-text">Clean tools that turn a web of connected systems into clear screens for the people who rely on them every single day.</p>
  <div class="ph featured-phone" role="img" aria-label="Hand holding a smartphone with an app open"></div>

  <div class="abs feature left" style="top:231px"><h4>Custom Software and Consulting</h4><p>Honest advice and tailored builds for each business process and goal.</p></div>
  <div class="abs feature-dot" style="left:392px;top:228px"><svg width="12" height="12" viewBox="0 0 12 12"><path d="M2 6l3 3 5-6" fill="none" stroke="#fff" stroke-width="1.8"/></svg></div>
  <div class="abs feature left" style="top:347px"><h4>Cutting edge Software Custom Designed</h4><p>Modern stacks chosen for speed, safety and a long working life.</p></div>
  <div class="abs feature-dot" style="left:392px;top:344px"><svg width="12" height="12" viewBox="0 0 12 12"><path d="M2 6l3 3 5-6" fill="none" stroke="#fff" stroke-width="1.8"/></svg></div>

  <div class="abs feature-dot" style="left:777px;top:228px"><svg width="12" height="12" viewBox="0 0 12 12"><path d="M2 6l3 3 5-6" fill="none" stroke="#fff" stroke-width="1.8"/></svg></div>
  <div class="abs feature right" style="top:231px"><h4>Modern, user Friendly Software</h4><p>Interfaces that need no manual and feel natural from the first day.</p></div>
  <div class="abs feature-dot" style="left:777px;top:344px"><svg width="12" height="12" viewBox="0 0 12 12"><path d="M2 6l3 3 5-6" fill="none" stroke="#fff" stroke-width="1.8"/></svg></div>
  <div class="abs feature right" style="top:347px"><h4>High end Web and Mobile Applications</h4><p>Robust apps that stay quick as your data and your team grow.</p></div>
</section>

<section class="contact">
  <h2 class="abs center contact-title">Keep In Touch <span>With Us</span></h2>
  <p class="abs contact-sub">Have a project in mind or a system that needs connecting? Send a short message and expect a reply within one day.</p>

  <div class="abs studio">
    <h4>NORTHGATE STUDIO</h4>
    <p>Independent software studio working with medium and large companies across Europe on integration and app projects.</p>
    <ul>
      <li><svg width="9" height="11" viewBox="0 0 9 11"><path d="M4.5 10.5S1 6.5 1 4.3a3.5 3.5 0 0 1 7 0c0 2.2-3.5 6.2-3.5 6.2z" fill="#555"/></svg>Kadeweg 14, Utrecht</li>
      <li><svg width="10" height="10" viewBox="0 0 10 10"><path d="M2 1l2 2-1 1.5a6 6 0 0 0 2.5 2.5L7 6l2 2-1.5 1.5C4 9 1 6 .5 2.5z" fill="#555"/></svg>Phone : +31 20 555 0147</li>
      <li><svg width="10" height="10" viewBox="0 0 10 10"><rect x="1" y="3" width="8" height="5" fill="#555"/><rect x="3" y="1" width="4" height="2" fill="#555"/></svg>Fax : +31 20 555 0148</li>
      <li><svg width="10" height="8" viewBox="0 0 10 8"><rect x=".5" y=".5" width="9" height="7" fill="none" stroke="#555"/><path d="M.5.5l4.5 4 4.5-4" fill="none" stroke="#555"/></svg>Email : hello@quarrymind.example</li>
    </ul>
    <div class="socials"><i></i><i></i><i></i><i></i><i></i><i></i></div>
  </div>

  <div class="abs field" style="top:197px;height:30px">Name</div>
  <div class="abs field" style="top:244px;height:30px">Email</div>
  <div class="abs field" style="top:288px;height:153px">Message</div>
  <div class="abs submit">SUBMIT</div>
</section>

<section class="map" role="img" aria-label="Street map of the city centre">
  <svg class="abs" style="left:196px;top:187px" width="20" height="26" viewBox="0 0 20 26"><path d="M10 25S1 14 1 9a9 9 0 0 1 18 0c0 5-9 16-9 16z" fill="var(--yellow)"/><circle cx="10" cy="9" r="3.5" fill="#fff"/></svg>
  <svg class="abs" style="left:593px;top:166px" width="20" height="26" viewBox="0 0 20 26"><path d="M10 25S1 14 1 9a9 9 0 0 1 18 0c0 5-9 16-9 16z" fill="var(--yellow)"/><circle cx="10" cy="9" r="3.5" fill="#fff"/></svg>
</section>

<footer class="site-footer">
  <div class="abs fcol" style="left:235px;width:170px">
    <div class="wordmark f-logo">Quarrymind</div>
    <p>Specialized software development from the Netherlands. Web apps, mobile apps and the logic that links your systems together.</p>
    <p style="margin-top:10px">Clear, simple and built to last for the people who use it daily.</p>
    <span class="f-link">Read More</span>
    <div class="follow">
      <div><i style="background:var(--blue)"></i>Follow Us<br>on Network</div>
      <div><i style="background:var(--yellow)"></i>Follow Us<br>on Network</div>
      <div><i style="background:var(--orange)"></i>Find Us<br>on Network</div>
      <div><i style="background:#5a6578"></i>Follow Us<br>on Network</div>
    </div>
  </div>

  <div class="abs fcol" style="left:420px;width:175px">
    <h5>Latest Blog</h5>
    <div class="post-mini"><i></i><div><b>Your Title Blog Here</b><small>Short note on linking systems.</small><small>22 December, 2015</small></div></div>
    <div class="post-mini"><i style="background:var(--blue)"></i><div><b>Your Title Blog Here</b><small>Short note on app design.</small><small>22 December, 2015</small></div></div>
    <div class="post-mini"><i></i><div><b>Your Title Blog Here</b><small>Short note on clean data.</small><small>22 December, 2015</small></div></div>
  </div>

  <div class="abs fcol" style="left:609px;width:175px">
    <h5>Tags Widget</h5>
    <div class="tags"><span>animation</span><span>beautiful</span><span>fine design</span><span>fun</span><span class="on">clothing</span><span>sexy</span></div>
    <h5 style="margin-top:30px">Useful Links</h5>
    <ul class="links"><li>Web App Development</li><li>Integrations</li><li>App Center</li><li>Order Account</li><li>Support Forum</li><li>Searchable App Books</li></ul>
  </div>

  <div class="abs fcol" style="left:794px;width:175px">
    <h5>Photo Widget</h5>
    <div class="photos"><i></i><i style="background:#6b7588"></i><i></i><i style="background:#6b7588"></i><i style="background:var(--blue)"></i><i></i><i></i><i style="background:#6b7588"></i><i></i></div>
    <h5 style="margin-top:26px">News Letter Widget</h5>
    <div class="news"><span>Your email here</span><i></i></div>
  </div>
</footer>

<div class="abs footer-bar" style="left:0;width:1200px">
  <div class="abs copy">© Copyright 2015 Quarrymind. All Rights Reserved.</div>
  <div class="abs bar-menu"><span class="current">Home</span><span>About</span><span>Portfolio</span><span>Blog</span><span>Features</span><span>Contact</span></div>
</div>

</body>
</html>
```